Spa needs a highly desired Membership Card

We need a membership card that captures people's desire to own it(our membership) when flashed by anyone! It should tell the "class" of the card owner!
Comes in Silver & Gold membership. Wants to have same design in different colour/tone to differentiate Gold & Silver.
Most members are woman, but we have few men as well.
Updates
Hi Designers,
Target Market(s)
Woman age 25-55 years old. High spending power in a relatively poor country(Myanmar).
They may be rich businesswomen, wives/daughters of rich man, women who are educated abroad and now return to home country as Myanmar is fast developing.
Requirements
Must have
- Must be in tiff, bmp or jpeg format so that card printer can recognise.
- TEXT
- Velmora Spa (font: Monotype Corsiva)
- No 82, Kintha Street, Mawlin Plaza (Level-5) (7716), Sanchaung Township, Yangon
- 09 47283916
- contactus@tervane-holdco.example
- A space for picture of card owner.
- No magnetic strip/smart chip.
- Name Abcdefghijklmn
- Membership No 12345678
- Expiry MM/YYYY
- For Gold:
- Terms and Conditions
- - Members enjoy 25% off all standard services, excluding promotional offers
- - Members enjoy 5% off for Lumivessa products, excluding promotional items
- - Members enjoy 10% off for all other retail products, excluding promotional items
- - 1 accompanying guest in a day enjoys 20% off standard services, excluding promotional offers
- - Memberships are valid for 2 years from the date of issue and are non-transferable
- - Memberships sold are non-refundable or exchangeable for cash, services or products
- - Privileges are subject to change without prior notice
- For Silver:
- Terms and Conditions
- - Members enjoy 20% off all standard services, excluding promotional offers
- I uploaded 2 of our spa pictures so you can have a feel our of premise. And uploaded our name card, I agree its not stylish as I designed it myself.

```html
<!DOCTYPE html>
<html lang="en">
<head>
<meta charset="utf-8">
<title>Velmora Spa Membership Cards</title>
<link rel="stylesheet" href="https://fonts.googleapis.com/css2?family=Josefin+Sans:wght@400;600&family=Cormorant+Garamond:ital,wght@1,600&display=swap">
<style>
  :root {
    --page: #ececea;
    --wood: #4a3426;
    --wood-dark: #2f2119;
    --gold-light: #f3dca0;
    --gold: #d6ab5e;
    --gold-deep: #a9793a;
    --silver-light: #ffffff;
    --silver: #d9d9d9;
    --silver-deep: #9c9c9c;
    --ink-dark: #2b1d14;
    --cream: #f1e6d6;
    --photo: #b89a86;
  }
  * { box-sizing: border-box; margin: 0; padding: 0; }
  html, body { width: 1200px; height: 794px; overflow: hidden; }
  body {
    background: var(--page);
    font-family: "Josefin Sans", sans-serif;
    position: relative;
  }
  .card {
    position: absolute;
    width: 520px;
    height: 326px;
    border-radius: 16px;
    overflow: hidden;
    background: var(--wood);
    box-shadow: 0 6px 16px rgba(0,0,0,.25);
  }
  .card--gold-info   { left: 50px;  top: 50px; }
  .card--silver-info { left: 630px; top: 50px; }
  .card--gold-front  { left: 50px;  top: 418px; }
  .card--silver-front{ left: 630px; top: 418px; }

  .gold   { --metal-a: var(--gold-light); --metal-b: var(--gold); --metal-c: var(--gold-deep); --title: var(--gold); }
  .silver { --metal-a: var(--silver-light); --metal-b: var(--silver); --metal-c: var(--silver-deep); --title: #ffffff; }

  .metal { background: linear-gradient(120deg, var(--metal-c) 0%, var(--metal-a) 40%, var(--metal-b) 65%, var(--metal-a) 85%, var(--metal-c) 100%); }

  /* info side */
  .info__crest {
    position: absolute; left: 330px; top: 0; width: 190px; height: 72px;
    display: flex; align-items: center; justify-content: center; gap: 8px;
  }
  .brand-mark { display: flex; align-items: center; gap: 7px; color: var(--wood-dark); font-weight: 600; font-size: 13px; letter-spacing: .5px; }
  .brand-mark__square { width: 12px; height: 12px; border: 2px solid currentColor; }
  .info__web {
    position: absolute; left: 330px; top: 72px; width: 190px; height: 40px;
    background: var(--wood-dark); color: var(--metal-a);
    font-size: 10px; line-height: 15px; text-align: right; padding: 5px 12px 0 0;
  }
  .info__contact {
    position: absolute; left: 330px; top: 112px; width: 190px; height: 214px;
    color: var(--ink-dark); font-size: 11.5px; line-height: 16px; padding: 10px 12px 0 12px;
  }
  .info__contact .role { text-decoration: underline; }
  .info__contact .rule { border-bottom: 1px solid var(--ink-dark); margin-top: 6px; width: 160px; }
  .info__title {
    position: absolute; left: 20px; top: 54px;
    color: var(--title); font-size: 22px; font-weight: 600; letter-spacing: .5px;
  }
  .info__name {
    position: absolute; left: 0; top: 92px; width: 330px; height: 40px;
    color: var(--ink-dark); font-size: 19px; padding: 11px 0 0 30px;
  }
  .info__photo {
    position: absolute; left: 22px; top: 150px; width: 120px; height: 160px;
    background: linear-gradient(180deg, #8d7464, var(--photo) 60%, #e8ddd5);
    border: 3px solid var(--cream);
  }
  .info__terms {
    position: absolute; left: 152px; top: 142px; width: 170px;
    color: var(--cream); font-size: 11.5px; line-height: 15.5px;
  }
  .info__terms h3 { font-weight: 400; font-size: 11.5px; text-decoration: underline; }
  .info__terms .rule { border-bottom: 1px solid var(--cream); margin-top: 3px; }

  /* front side */
  .front__pattern {
    position: absolute; inset: 0;
    background: radial-gradient(ellipse at 50% 45%, #4f3829 0%, var(--wood) 55%, var(--wood-dark) 100%);
  }
  .front__content {
    position: absolute; inset: 0;
    display: flex; flex-direction: column; align-items: center; justify-content: center;
  }
  .front .brand-mark { color: var(--title); font-size: 15px; margin-bottom: 14px; }
  .front .brand-mark__square { width: 16px; height: 16px; }
  .front__title { color: var(--title); font-size: 38px; font-weight: 400; letter-spacing: .5px; }
  .front__script {
    color: var(--title); font-family: "Cormorant Garamond", serif; font-style: italic;
    font-weight: 600; font-size: 28px; margin-top: 2px;
  }
</style>
</head>
<body>

  <!-- Gold info side -->
  <section class="card card--gold-info gold">
    <div class="info__crest metal"><span class="brand-mark"><span class="brand-mark__square"></span>Velmora Spa</span></div>
    <div class="info__web">T : 09 47283916<br>WWW.VELMORASPA.EXAMPLE</div>
    <div class="info__contact metal">
      <div class="role">Kaung Zaw Lin : Director</div>
      (959) 448203615 (YGN)<br>(65) 97316482 (SCP)<br>kzl@tervane-holdco.example<br>No 82, Kintha Street,<br>Mawlin Plaza (Level-5),<br>Sanchaung Township, Yangon.<br>(7716).
      <div class="rule"></div>
    </div>
    <h2 class="info__title">GOLD MEMBERSHIP</h2>
    <div class="info__name metal">Customers Name</div>
    <div class="info__photo" role="img" aria-label="Portrait photo of the card owner"></div>
    <div class="info__terms">
      <h3>Terms and Conditions</h3>
      blah blah blah blah blah<br>blah blah blah blah blah<br>blah blah blah blah blah<br>blah blah blah blah blah<br>blah blah blah blah blah<br>blah blah blah blah blah<br>blah blah blah blah blah<br>blah blah blah blah blah
      <div class="rule"></div>
    </div>
  </section>

  <!-- Silver info side -->
  <section class="card card--silver-info silver">
    <div class="info__crest metal"><span class="brand-mark"><span class="brand-mark__square"></span>Velmora Spa</span></div>
    <div class="info__web">T : 09 47283916<br>WWW.VELMORASPA.EXAMPLE</div>
    <div class="info__contact metal">
      <div class="role">Kaung Zaw Lin : Director</div>
      (959) 448203615 (YGN)<br>(65) 97316482 (SCP)<br>kzl@tervane-holdco.example<br>No 82, Kintha Street,<br>Mawlin Plaza (Level-5),<br>Sanchaung Township, Yangon.<br>(7716).
      <div class="rule"></div>
    </div>
    <h2 class="info__title">SILVER MEMBERSHIP</h2>
    <div class="info__name metal">Customers Name</div>
    <div class="info__photo" role="img" aria-label="Portrait photo of the card owner"></div>
    <div class="info__terms">
      <h3>Terms and Conditions</h3>
      blah blah blah blah blah<br>blah blah blah blah blah<br>blah blah blah blah blah<br>blah blah blah blah blah<br>blah blah blah blah blah<br>blah blah blah blah blah<br>blah blah blah blah blah<br>blah blah blah blah blah
      <div class="rule"></div>
    </div>
  </section>

  <!-- Gold front -->
  <section class="card card--gold-front front gold">
    <div class="front__pattern" role="img" aria-label="Dark brown damask pattern over wood texture"></div>
    <div class="front__content">
      <span class="brand-mark"><span class="brand-mark__square"></span>Velmora Spa</span>
      <h1 class="front__title">GOLD MEMBERSHIP</h1>
      <p class="front__script">Velmora Spa</p>
    </div>
  </section>

  <!-- Silver front -->
  <section class="card card--silver-front front silver">
    <div class="front__pattern" role="img" aria-label="Dark brown damask pattern over wood texture"></div>
    <div class="front__content">
      <span class="brand-mark"><span class="brand-mark__square"></span>Velmora Spa</span>
      <h1 class="front__title">SILVER MEMBERSHIP</h1>
      <p class="front__script">Velmora Spa</p>
    </div>
  </section>

</body>
</html>
```